<作成物>
■リッチメッセージ
リッチメニュー
合計2枚

【デザインの詳細】
デザインのイメージをファイルに入れております。
ロゴと・イメージのデザイン合わせた感じにしていただけると嬉しいです。
上下で一体感があるものを希望します。
https://22.datavault.test/0917-8a3c61f0b2d94e57c0a1d83e6b7f2c95

〈リッチメニューの表示項目〉
画像の中に入れますの、これを参考に入れてください。
この画像に似た物を作成してほしいというわけではありません。

デザイン重視でここの表示名はデザイン的に英語の方がよければ
英語でも大丈夫です。意味がわかって
ニュアンスがあっていれば文字を短くするのも
お任せします。あくまでデザイン重視です。
〈画像はこちらから〉

※こちらの作成以外に勝手に使用された場合は
著作権侵害で法的手段をとらせていただきます。
作成事例にもしようしないでください。

<サイズ>
・リッチメッセージ(1040×1040ピクセル)
・リッチメニュー(1200×810ピクセル)

<納品形式>
・ai形式(イラストレーターデータ)
・JPG
<詳細>
※添付ファイルをご確認ください。

<備考>
ブランディング効果を期待しています。
どんどん何個でも応募ください。

```html
<!DOCTYPE html>
<html lang="ja">
<head>
<meta charset="utf-8">
<title>Nagi セラピー&amp;スクール リッチメッセージ・リッチメニュー</title>
<link rel="stylesheet" href="https://fonts.googleapis.com/css2?family=Noto+Serif+JP:wght@400;600&family=Cormorant+Garamond:wght@500;600&display=swap">
<style>
:root{
  --page:#ffffff;
  --ink:#1f1a22;
  --panel-top:#d9c8ea;
  --panel-mid:#f1d7ea;
  --panel-low:#e6c4e4;
  --hex-a:#e98ac4;
  --hex-b:#d56fb2;
  --cell-a:#d8cbe9;
  --cell-b:#f4cde0;
  --cell-line:#d3c3dc;
  --band:rgba(255,255,255,.78);
  --brand:#8d6aa6;
}
*{box-sizing:border-box;margin:0;padding:0}
html,body{width:798px;height:1200px;overflow:hidden;background:var(--page)}
body{position:relative;font-family:"Noto Serif JP",serif;color:var(--ink)}

.message{position:absolute;left:48px;top:13px;width:729px;height:640px;overflow:hidden;
  background:linear-gradient(160deg,var(--panel-top) 0%,var(--panel-mid) 55%,var(--panel-low) 100%)}
.message__floral{position:absolute;inset:0;
  background:radial-gradient(circle at 82% 22%,rgba(255,255,255,.55),transparent 40%),
             radial-gradient(circle at 15% 80%,rgba(255,255,255,.45),transparent 42%)}
.brand{position:absolute;left:26px;top:26px;font-family:"Cormorant Garamond",serif;font-weight:600;
  font-size:34px;color:var(--brand);display:flex;align-items:center;gap:8px}
.brand__dot{width:12px;height:12px;border-radius:50%;background:var(--brand)}
.headline{position:absolute;left:0;right:0;top:168px;height:64px;background:var(--band);
  display:flex;align-items:center;justify-content:center;font-size:33px;font-weight:600;letter-spacing:1px}
.services{position:absolute;left:0;top:0;width:729px;height:640px}
.hex-label{font-family:"Noto Serif JP",serif;fill:#fff;text-anchor:middle}
.hex-label--en{font-family:"Cormorant Garamond",serif;font-weight:600;font-size:20px}
.hex-label--jp{font-size:16px}

.menu{position:absolute;left:48px;top:697px;width:729px;height:468px;
  display:grid;grid-template-columns:repeat(3,1fr);grid-template-rows:repeat(2,1fr);gap:10px}
.cell{position:relative;border:2px solid var(--cell-line);overflow:hidden;
  background:linear-gradient(145deg,var(--cell-a),var(--cell-b));
  display:flex;flex-direction:column;align-items:center;justify-content:flex-start;padding-top:22px}
.cell__title{font-family:"Cormorant Garamond",serif;font-weight:600;font-size:30px;line-height:1;text-align:center}
.cell__icon{margin-top:26px}
.store{justify-content:center;padding-top:0}
.store__floral{position:absolute;inset:0;background:linear-gradient(135deg,#faf7fa,#ece3ee)}
.store__lead,.store__name,.store__branch{position:relative}
.store__lead{font-size:20px;align-self:flex-start;margin-left:18px}
.store__name{font-family:"Cormorant Garamond",serif;font-weight:600;font-size:56px;line-height:1.1;margin-top:6px}
.store__branch{font-size:18px}
</style>
</head>
<body>

<section class="message">
  <div class="message__floral" role="img" aria-label="淡い線画の花と光のぼかしの背景"></div>
  <div class="brand"><span class="brand__dot"></span>Nagi</div>
  <h1 class="headline">カラダのメンテナンスしてますか？</h1>
  <svg class="services" viewBox="0 0 729 640">
    <defs>
      <linearGradient id="hexFill" x1="0" y1="0" x2="0" y2="1">
        <stop offset="0" stop-color="#e98ac4" stop-opacity=".92"/>
        <stop offset="1" stop-color="#d56fb2" stop-opacity=".92"/>
      </linearGradient>
      <polygon id="hex" points="82,0 164,47 164,141 82,188 0,141 0,47"/>
    </defs>
    <g transform="translate(269,240)">
      <use href="#hex" fill="url(#hexFill)"/>
      <text class="hex-label hex-label--en" x="82" y="88">Hair Removal</text>
      <text class="hex-label hex-label--jp" x="82" y="112">光脱毛</text>
    </g>
    <g transform="translate(185,387)">
      <use href="#hex" fill="url(#hexFill)"/>
      <text class="hex-label hex-label--en" x="82" y="78">Eyelash</text>
      <text class="hex-label hex-label--en" x="82" y="100">Extension</text>
      <text class="hex-label hex-label--jp" x="82" y="122">まつ毛エクステ</text>
    </g>
    <g transform="translate(353,387)">
      <use href="#hex" fill="url(#hexFill)"/>
      <text class="hex-label hex-label--en" x="82" y="88">Skin Peeling</text>
      <text class="hex-label hex-label--jp" x="82" y="112">ピーリング</text>
    </g>
  </svg>
</section>

<nav class="menu">
  <div class="cell store">
    <div class="store__floral" role="img" aria-label="淡い線画の花の背景"></div>
    <span class="store__lead">セラピー&amp;スクール</span>
    <span class="store__name">Nagi</span>
    <span class="store__branch">港町店</span>
  </div>
  <div class="cell">
    <span class="cell__title">SNS</span>
    <svg class="cell__icon" width="90" height="120" viewBox="0 0 90 120" fill="none" stroke="#1f1a22" stroke-width="5">
      <rect x="8" y="4" width="74" height="112" rx="8"/>
      <line x1="8" y1="96" x2="82" y2="96"/>
      <circle cx="45" cy="106" r="3" fill="#1f1a22" stroke="none"/>
      <circle cx="45" cy="50" r="24" stroke-width="3.5"/>
      <ellipse cx="45" cy="50" rx="10" ry="24" stroke-width="3"/>
      <line x1="21" y1="50" x2="69" y2="50" stroke-width="3"/>
    </svg>
  </div>
  <div class="cell">
    <span class="cell__title">School<br>Information</span>
    <svg class="cell__icon" width="90" height="90" viewBox="0 0 90 90" fill="#1f1a22">
      <path d="M42 80 C40 50 28 36 4 34 C6 60 22 72 42 70 Z"/>
      <path d="M48 80 C50 46 62 26 86 20 C86 52 72 66 48 66 Z"/>
      <rect x="42" y="60" width="6" height="28"/>
    </svg>
  </div>
  <div class="cell store">
    <div class="store__floral" role="img" aria-label="淡い線画の花の背景"></div>
    <span class="store__lead">セラピー&amp;スクール</span>
    <span class="store__name">Nagi</span>
    <span class="store__branch">緑ヶ丘店</span>
  </div>
  <div class="cell">
    <span class="cell__title">Introduce</span>
    <svg class="cell__icon" width="110" height="110" viewBox="0 0 110 110" fill="#1f1a22" stroke="#1f1a22" stroke-width="7">
      <line x1="26" y1="55" x2="84" y2="22"/>
      <line x1="26" y1="55" x2="84" y2="88"/>
      <circle cx="26" cy="55" r="15" stroke="none"/>
      <circle cx="84" cy="22" r="15" stroke="none"/>
      <circle cx="84" cy="88" r="15" stroke="none"/>
    </svg>
  </div>
  <div class="cell">
    <span class="cell__title">Reserve</span>
    <svg class="cell__icon" width="100" height="100" viewBox="0 0 100 100" fill="#1f1a22">
      <path d="M22 10 L38 30 L30 42 C36 56 46 66 58 72 L70 62 L90 78 L80 92 C50 92 10 52 8 22 Z"/>
      <path d="M56 30 A16 16 0 0 1 70 44" fill="none" stroke="#1f1a22" stroke-width="5"/>
      <path d="M58 14 A32 32 0 0 1 86 42" fill="none" stroke="#1f1a22" stroke-width="5"/>
    </svg>
  </div>
</nav>

</body>
</html>
```